Storm in companies

Cover for the book "Count the quiet hours", a thriller on social aspects of big companies: suicides among employees of a computer company, murders among rich and powerful leaders of several big companies.

Target Market(s)

Thriller readers (with an interest in social aspects of companies)

Industry/Entity Type

Publishing

Colors

Designer to choose colors to be used in the design.

Requirements
Must have
• Size: 14 x 20.5 cm (bleed)
Nice to have
• A storm and buildings, but other ideas are welcome.

```html
<!DOCTYPE html>
<html lang="en">
<head>
<meta charset="utf-8">
<title>Count the quiet hours — cover</title>
<link rel="stylesheet" href="https://fonts.googleapis.com/css2?family=Bebas+Neue&family=Oswald:wght@500;600&display=swap">
<style>
  :root {
    --page-bg: #e4e7e8;
    --cover-cream: #e6dccb;
    --panel-grey: #7c7a78;
    --panel-grey-dark: #6b6967;
    --ink-light: #ebe3d5;
    --ink-black: #121212;
    --photo-light: #d9d6d2;
    --photo-mid: #a9a6a2;
  }
  * { box-sizing: border-box; margin: 0; padding: 0; }
  html, body {
    width: 1200px; height: 800px; overflow: hidden;
    background: var(--page-bg);
  }
  .stage {
    width: 1200px; height: 800px;
    display: flex; align-items: center; justify-content: center;
  }
  .cover {
    position: relative;
    width: 492px; height: 720px;
    background: var(--cover-cream);
  }
  .cover-panel {
    position: absolute;
    left: 50px; top: 45px; right: 22px; bottom: 25px;
    background: var(--panel-grey);
    overflow: hidden;
  }
  .cover-photo {
    position: absolute;
    left: 0; right: 0; top: 300px; bottom: 0;
    background:
      radial-gradient(ellipse at 50% 60%, var(--photo-light) 0%, var(--photo-mid) 55%, var(--panel-grey) 100%),
      linear-gradient(to bottom, var(--panel-grey), var(--photo-mid));
  }
  .title-top {
    position: absolute;
    left: 171px; top: 47px; right: 0; height: 75px;
    background: var(--panel-grey-dark);
    border: 3px solid var(--ink-light);
    border-right: none;
    display: flex; align-items: center; justify-content: center;
    font-family: "Oswald", sans-serif; font-weight: 600;
    font-size: 46px; letter-spacing: 1px;
    color: var(--ink-light);
  }
  .title-main {
    position: absolute;
    left: 38px; top: 108px;
    font-family: "Bebas Neue", sans-serif;
    font-size: 210px; line-height: 0.85;
    color: var(--ink-light);
    letter-spacing: -2px;
  }
  .title-bottom {
    position: absolute;
    left: 115px; top: 292px; right: 0; height: 74px;
    background: var(--ink-black);
    display: flex; align-items: center; justify-content: center;
    font-family: "Oswald", sans-serif; font-weight: 600;
    font-size: 58px; letter-spacing: 3px;
    color: var(--ink-light);
  }
</style>
</head>
<body>
  <main class="stage">
    <article class="cover">
      <div class="cover-panel">
        <div class="cover-photo" role="img" aria-label="Photograph of an office worker standing amid a whirl of flying papers, in grey tones"></div>
        <h1 class="cover-title">
          <span class="title-top">COUNT THE</span>
          <span class="title-main">QUIET</span>
          <span class="title-bottom">HOURS</span>
        </h1>
      </div>
    </article>
  </main>
</body>
</html>
```